PSD for Magento Site (No Code Required)

I Need 10 pages design for a new Plus-Size Lingerie Site. The site has to be a edgy, fun & clean.

I will need versions of each page for mobile, tablet sizes as well. We are trying to be a new kind of lingerie site. something non traditional. A Fun place to show. Big images, Easy Navigation, Simple Layout.

Full Brief is Attached.

Target Market(s)

Plus size Women, Lingerie Enthusiasts

Industry/Entity Type

Retail

Number of Pages Required

5+ page

Font styles to use
Sans Serif

Colors
000000
ffffff
d3d3d3

Requirements
Must have
• Well Structured Mobile versions of each page
Should not have
• clutter

```html
<!DOCTYPE html>
<html lang="en">
<head>
<meta charset="utf-8">
<title>Fullbloom Lingerie — Home</title>
<link href="https://fonts.googleapis.com/css2?family=Raleway:wght@300;400;500;600;700&display=swap" rel="stylesheet">
<style>
:root{
  --black:#000000;
  --white:#ffffff;
  --orange:#f39a3d;
  --orange-deep:#e08a30;
  --orange-active:#c9782a;
  --grey-light:#d3d3d3;
  --grey-band:#efefef;
  --grey-btn:#8a8a8a;
  --grey-dark:#555555;
  --text:#222222;
  --price:#e0822a;
  --cyan:#4cc9d8;
  --hero-grey:#c9c9cc;
}
*{margin:0;padding:0;box-sizing:border-box}
html,body{width:1200px;height:2381px;overflow:hidden}
body{position:relative;background:var(--white);font-family:'Raleway',sans-serif;color:var(--text)}
.abs{position:absolute}

/* Header */
.site-header{position:absolute;left:0;top:0;width:1200px;height:135px;background:var(--black)}
.brand{position:absolute;left:98px;top:24px;color:var(--white)}
.brand-name{font-size:50px;font-weight:600;letter-spacing:1px;line-height:1}
.brand-tag{font-size:15px;font-weight:400;letter-spacing:23px;margin-top:12px;padding-left:22px}
.cart{position:absolute;left:818px;top:32px;display:flex;align-items:center;gap:9px;color:var(--white);font-size:15px}
.cart-icon{width:27px;height:27px;border-radius:50%;background:var(--orange);display:flex;align-items:center;justify-content:center}
.checkout{position:absolute;left:982px;top:32px;display:flex;align-items:center;gap:9px;color:var(--white);font-size:15px}
.checkout-icon{width:27px;height:27px;border-radius:50%;background:#6f8fc8;display:flex;align-items:center;justify-content:center}
.search{position:absolute;left:932px;top:81px;width:170px;height:30px;border:1px solid var(--white);color:var(--white);font-size:13px;padding:6px 9px}
.search svg{position:absolute;right:9px;top:8px}

/* Nav */
.main-nav{position:absolute;left:0;top:135px;width:1200px;height:70px;background:var(--orange)}
.main-nav ul{list-style:none;display:flex;position:absolute;left:98px;top:0;height:70px}
.main-nav li{height:70px;display:flex;align-items:center;color:var(--white);font-size:13px;font-weight:500;padding:0 28px}
.main-nav li.active{background:var(--orange-active);width:119px;justify-content:center;padding:0}

/* Hero */
.hero{position:absolute;left:0;top:205px;width:1200px;height:482px}
.hero-art{position:absolute;inset:0}
.hero-logo{position:absolute;left:454px;top:163px;width:327px;height:57px;background:#1a1a1a;color:var(--white);font-size:43px;font-weight:600;text-align:center;line-height:57px;letter-spacing:1px}
.hero-tag{position:absolute;left:454px;top:226px;width:327px;text-align:center;color:#222;font-size:14px;letter-spacing:22px;padding-left:22px}
.hero-lines{position:absolute;right:419px;top:290px;text-align:right;color:#4a4a4a;font-size:25px;font-weight:600;line-height:36px}
.hero-arrow{position:absolute;top:225px;width:35px;height:34px;background:#4d5a60;display:flex;align-items:center;justify-content:center}

/* Category tiles */
.tile{position:absolute;top:709px;height:218px;border-radius:4px;overflow:hidden}
.tile-bar{position:absolute;left:0;bottom:0;width:100%;height:60px;display:flex;align-items:center;justify-content:space-between;padding:0 16px 0 17px;color:var(--white);font-size:18px;font-weight:600}
.tile-bar.dark{background:rgba(20,20,20,.88)}
.tile-bar.orange{background:rgba(243,154,61,.92)}

/* Product sections */
.section-head{position:absolute;left:114px;width:970px;border-bottom:2px solid #555;height:32px}
.section-head h2{font-size:20px;font-weight:600;color:#111;line-height:22px}
.pager{position:absolute;right:0;top:0;display:flex;gap:3px}
.pager span{width:24px;height:22px;background:var(--grey-light);display:flex;align-items:center;justify-content:center}
.product{position:absolute;width:222px}
.product-photo{width:222px;height:241px;border:1px solid #ddd;padding:4px;background:var(--white)}
.product-photo div{width:100%;height:100%}
.product-name{font-size:14px;margin-top:14px;color:#111}
.product-price{font-size:13px;font-weight:600;color:var(--price);margin-top:8px}
.product-actions{display:flex;gap:13px;margin-top:14px}
.btn-cart{width:110px;height:29px;color:var(--white);font-size:12px;display:flex;align-items:center;justify-content:center;background:var(--grey-btn)}
.btn-cart.primary{background:var(--orange)}
.btn-icon{width:35px;height:29px;border:1px solid #bbb;display:flex;align-items:center;justify-content:center}

/* Perks */
.perks{position:absolute;left:0;top:1833px;width:1200px;height:160px;background:var(--grey-band)}
.perk{position:absolute;top:27px;width:284px;height:108px;border:2px solid #c8c8c8;background:var(--white);padding:16px 0 0 15px}
.perk h3{font-size:20px;font-weight:600;line-height:24px;color:#111}
.perk p{font-size:12px;font-weight:600;color:var(--price);margin-top:6px}
.perk-icon{position:absolute;right:15px;top:27px;width:57px;height:57px;border-radius:50%;display:flex;align-items:center;justify-content:center}

/* Footer */
.site-footer{position:absolute;left:0;top:1993px;width:1200px;height:388px;background:var(--black);color:var(--white)}
.footer-col{position:absolute;top:26px}
.footer-col h4{font-size:17px;font-weight:500;padding-bottom:8px;position:relative}
.footer-col h4::after{content:"";position:absolute;left:0;bottom:0;width:88px;height:2px;background:var(--orange-deep)}
.footer-col ul{list-style:none;margin-top:14px}
.footer-col li{font-size:13px;line-height:28.3px}
.socials{display:flex;gap:13px;margin-top:18px}
.socials span{width:28px;height:28px;border:1px solid var(--white);border-radius:50%}
.cards{display:flex;gap:5px;margin-top:18px}
.cards span{width:41px;height:27px;border-radius:2px}
.news-text{font-size:13px;line-height:19px;margin-top:14px;width:220px}
.news-input{width:216px;height:30px;background:var(--white);color:#999;font-size:12px;padding:7px 8px;margin-top:9px}
.news-btn{width:104px;height:30px;background:var(--orange-deep);font-size:13px;display:flex;align-items:center;justify-content:center;margin-top:13px}
.footer-wave{position:absolute;left:0;bottom:0}
.copyright{position:absolute;left:98px;top:351px;font-size:14px}
.footer-brand{position:absolute;left:849px;top:292px;text-align:center;width:254px}
.footer-brand .brand-name{font-size:40px;font-weight:600;letter-spacing:1px}
.footer-brand .brand-tag{font-size:12px;letter-spacing:19px;margin-top:8px;padding-left:19px}
</style>
</head>
<body>

<header class="site-header">
  <div class="brand">
    <div class="brand-name">FULLBLOOM</div>
    <div class="brand-tag">LINGERIE</div>
  </div>
  <div class="cart">
    <span class="cart-icon"><svg width="14" height="12" viewBox="0 0 14 12"><path d="M0 1h2.5l2 7h7l2-5H4" fill="none" stroke="#fff" stroke-width="1.5"/><circle cx="5.5" cy="10.5" r="1.2" fill="#fff"/><circle cx="10.5" cy="10.5" r="1.2" fill="#fff"/></svg></span>
    0 ITEMS - $0.00
  </div>
  <div class="checkout">
    <span class="checkout-icon"><svg width="12" height="12" viewBox="0 0 12 12"><path d="M1 6h8M6 2l4 4-4 4" fill="none" stroke="#fff" stroke-width="1.8"/></svg></span>
    CHECKOUT
  </div>
  <div class="search">Search
    <svg width="13" height="13" viewBox="0 0 13 13"><circle cx="5" cy="5" r="4" fill="none" stroke="#fff" stroke-width="1.8"/><path d="M8 8l4 4" stroke="#fff" stroke-width="2"/></svg>
  </div>
</header>

<nav class="main-nav">
  <ul>
    <li class="active">HOME</li>
    <li>LINGERIE</li>
    <li>COSTUMES</li>
    <li>PANTIES</li>
    <li>DRESSES</li>
    <li>SLEEPWEAR</li>
    <li>HOSIERY</li>
    <li>ACCESSORIES</li>
  </ul>
</nav>

<section class="hero">
  <svg class="hero-art" width="1200" height="482" role="img" aria-label="Banner photo: two models in lingerie, one on a turquoise background at left and one on a grey background at right">
    <defs>
      <linearGradient id="heroCyan" x1="0" y1="0" x2="1" y2="1"><stop offset="0" stop-color="#5fd6e2"/><stop offset="1" stop-color="#34b7c9"/></linearGradient>
      <linearGradient id="heroGrey" x1="0" y1="0" x2="1" y2="0"><stop offset="0" stop-color="#d6d6d9"/><stop offset="1" stop-color="#bdbdc1"/></linearGradient>
    </defs>
    <rect width="1200" height="482" fill="url(#heroGrey)"/>
    <polygon points="0,0 648,0 548,482 0,482" fill="url(#heroCyan)"/>
  </svg>
  <div class="hero-logo">FULLBLOOM</div>
  <div class="hero-tag">LINGERIE</div>
  <div class="hero-lines">LINGERIES<br>DRESSES<br>SLEEPWEAR</div>
  <div class="hero-arrow" style="left:13px"><svg width="10" height="14" viewBox="0 0 10 14"><path d="M8 1L2 7l6 6" fill="none" stroke="#fff" stroke-width="1.6"/></svg></div>
  <div class="hero-arrow" style="left:1152px"><svg width="10" height="14" viewBox="0 0 10 14"><path d="M2 1l6 6-6 6" fill="none" stroke="#fff" stroke-width="1.6"/></svg></div>
</section>

<a class="tile" style="left:114px;width:267px;background:linear-gradient(135deg,#8e8e92,#3a3a3e)" role="img" aria-label="Photo: model in a black lingerie set">
  <span class="tile-bar dark">LINGIRIE SETS <svg width="17" height="17" viewBox="0 0 17 17"><circle cx="8.5" cy="8.5" r="8.5" fill="#fff"/><path d="M5 8.5h6M8.5 5.5l3 3-3 3" fill="none" stroke="#222" stroke-width="1.8"/></svg></span>
</a>
<a class="tile" style="left:397px;width:270px;background:linear-gradient(160deg,#3f5f86,#2a3a5e)" role="img" aria-label="Photo: model in a blue swim set">
  <span class="tile-bar orange">SWIMMER SETS <svg width="17" height="17" viewBox="0 0 17 17"><circle cx="8.5" cy="8.5" r="8.5" fill="#fff"/><path d="M5 8.5h6M8.5 5.5l3 3-3 3" fill="none" stroke="#e08a30" stroke-width="1.8"/></svg></span>
</a>
<a class="tile" style="left:679px;width:405px;background:linear-gradient(135deg,#6c6c70,#2e2e31)" role="img" aria-label="Photo: couple posing in lingerie">
  <span class="tile-bar dark">SHOP LINGERIES <svg width="17" height="17" viewBox="0 0 17 17"><circle cx="8.5" cy="8.5" r="8.5" fill="#fff"/><path d="M5 8.5h6M8.5 5.5l3 3-3 3" fill="none" stroke="#222" stroke-width="1.8"/></svg></span>
</a>

<!-- Featured products -->
<div class="section-head" style="top:966px">
  <h2>FEATURED PRODUCTS</h2>
  <div class="pager"><span><svg width="7" height="11"><path d="M6 1L1.5 5.5 6 10" fill="none" stroke="#fff" stroke-width="1.5"/></svg></span><span><svg width="7" height="11"><path d="M1 1l4.5 4.5L1 10" fill="none" stroke="#fff" stroke-width="1.5"/></svg></span></div>
</div>

<div class="product" style="left:116px;top:1024px">
  <div class="product-photo"><div role="img" aria-label="Product photo: black sheer babydoll" style="background:linear-gradient(160deg,#e4e1dc,#2c2c2c)"></div></div>
  <p class="product-name">Nascetur ridiculus mus</p><p class="product-price">$125.00</p>
  <div class="product-actions"><span class="btn-cart primary">Add to Cart</span><span class="btn-icon"><svg width="13" height="12" viewBox="0 0 13 12"><path d="M6.5 11L1.3 5.8A3 3 0 016.5 1.8a3 3 0 015.2 4z" fill="#333"/></svg></span><span class="btn-icon"><svg width="12" height="12"><circle cx="5" cy="5" r="3.8" fill="none" stroke="#333" stroke-width="1.6"/><path d="M8 8l3 3" stroke="#333" stroke-width="1.8"/></svg></span></div>
</div>
<div class="product" style="left:365px;top:1024px">
  <div class="product-photo"><div role="img" aria-label="Product photo: red corset" style="background:linear-gradient(160deg,#a9a4a0,#c8262b)"></div></div>
  <p class="product-name">Nascetur ridiculus mus</p><p class="product-price">$125.00</p>
  <div class="product-actions"><span class="btn-cart">Add to Cart</span><span class="btn-icon"><svg width="13" height="12" viewBox="0 0 13 12"><path d="M6.5 11L1.3 5.8A3 3 0 016.5 1.8a3 3 0 015.2 4z" fill="#333"/></svg></span><span class="btn-icon"><svg width="12" height="12"><circle cx="5" cy="5" r="3.8" fill="none" stroke="#333" stroke-width="1.6"/><path d="M8 8l3 3" stroke="#333" stroke-width="1.8"/></svg></span></div>
</div>
<div class="product" style="left:614px;top:1024px">
  <div class="product-photo"><div role="img" aria-label="Product photo: black chemise outdoors" style="background:linear-gradient(160deg,#5d7a3a,#1e1e1e)"></div></div>
  <p class="product-name">Nascetur ridiculus mus</p><p class="product-price">$125.00</p>
  <div class="product-actions"><span class="btn-cart">Add to Cart</span><span class="btn-icon"><svg width="13" height="12" viewBox="0 0 13 12"><path d="M6.5 11L1.3 5.8A3 3 0 016.5 1.8a3 3 0 015.2 4z" fill="#333"/></svg></span><span class="btn-icon"><svg width="12" height="12"><circle cx="5" cy="5" r="3.8" fill="none" stroke="#333" stroke-width="1.6"/><path d="M8 8l3 3" stroke="#333" stroke-width="1.8"/></svg></span></div>
</div>
<div class="product" style="left:863px;top:1024px">
  <div class="product-photo"><div role="img" aria-label="Product photo: black and pink bustier" style="background:linear-gradient(160deg,#b9c4c9,#2a2a2e 60%,#d6337a)"></div></div>
  <p class="product-name">Nascetur ridiculus mus</p><p class="product-price">$125.00</p>
  <div class="product-actions"><span class="btn-cart">Add to Cart</span><span class="btn-icon"><svg width="13" height="12" viewBox="0 0 13 12"><path d="M6.5 11L1.3 5.8A3 3 0 016.5 1.8a3 3 0 015.2 4z" fill="#333"/></svg></span><span class="btn-icon"><svg width="12" height="12"><circle cx="5" cy="5" r="3.8" fill="none" stroke="#333" stroke-width="1.6"/><path d="M8 8l3 3" stroke="#333" stroke-width="1.8"/></svg></span></div>
</div>

<!-- New arrivals -->
<div class="section-head" style="top:1409px">
  <h2>NEW ARRIVALS</h2>
  <div class="pager"><span><svg width="7" height="11"><path d="M6 1L1.5 5.5 6 10" fill="none" stroke="#fff" stroke-width="1.5"/></svg></span><span><svg width="7" height="11"><path d="M1 1l4.5 4.5L1 10" fill="none" stroke="#fff" stroke-width="1.5"/></svg></span></div>
</div>

<div class="product" style="left:116px;top:1466px">
  <div class="product-photo"><div role="img" aria-label="Product photo: blue lace teddy" style="background:linear-gradient(160deg,#9fb0bf,#3549a8)"></div></div>
  <p class="product-name">Nascetur ridiculus mus</p><p class="product-price">$125.00</p>
  <div class="product-actions"><span class="btn-cart primary">Add to Cart</span><span class="btn-icon"><svg width="13" height="12" viewBox="0 0 13 12"><path d="M6.5 11L1.3 5.8A3 3 0 016.5 1.8a3 3 0 015.2 4z" fill="#333"/></svg></span><span class="btn-icon"><svg width="12" height="12"><circle cx="5" cy="5" r="3.8" fill="none" stroke="#333" stroke-width="1.6"/><path d="M8 8l3 3" stroke="#333" stroke-width="1.8"/></svg></span></div>
</div>
<div class="product" style="left:365px;top:1466px">
  <div class="product-photo"><div role="img" aria-label="Product photo: black corset with garters" style="background:linear-gradient(160deg,#eeeeee,#1f1f1f)"></div></div>
  <p class="product-name">Nascetur ridiculus mus</p><p class="product-price">$125.00</p>
  <div class="product-actions"><span class="btn-cart">Add to Cart</span><span class="btn-icon"><svg width="13" height="12" viewBox="0 0 13 12"><path d="M6.5 11L1.3 5.8A3 3 0 016.5 1.8a3 3 0 015.2 4z" fill="#333"/></svg></span><span class="btn-icon"><svg width="12" height="12"><circle cx="5" cy="5" r="3.8" fill="none" stroke="#333" stroke-width="1.6"/><path d="M8 8l3 3" stroke="#333" stroke-width="1.8"/></svg></span></div>
</div>
<div class="product" style="left:614px;top:1466px">
  <div class="product-photo"><div role="img" aria-label="Product photo: pink sheer babydoll" style="background:linear-gradient(160deg,#8fb46a,#f0c8c4)"></div></div>
  <p class="product-name">Nascetur ridiculus mus</p><p class="product-price">$125.00</p>
  <div class="product-actions"><span class="btn-cart">Add to Cart</span><span class="btn-icon"><svg width="13" height="12" viewBox="0 0 13 12"><path d="M6.5 11L1.3 5.8A3 3 0 016.5 1.8a3 3 0 015.2 4z" fill="#333"/></svg></span><span class="btn-icon"><svg width="12" height="12"><circle cx="5" cy="5" r="3.8" fill="none" stroke="#333" stroke-width="1.6"/><path d="M8 8l3 3" stroke="#333" stroke-width="1.8"/></svg></span></div>
</div>
<div class="product" style="left:863px;top:1466px">
  <div class="product-photo"><div role="img" aria-label="Product photo: black ruffled babydoll" style="background:linear-gradient(160deg,#f2f2f2,#262626)"></div></div>
  <p class="product-name">Nascetur ridiculus mus</p><p class="product-price">$125.00</p>
  <div class="product-actions"><span class="btn-cart">Add to Cart</span><span class="btn-icon"><svg width="13" height="12" viewBox="0 0 13 12"><path d="M6.5 11L1.3 5.8A3 3 0 016.5 1.8a3 3 0 015.2 4z" fill="#333"/></svg></span><span class="btn-icon"><svg width="12" height="12"><circle cx="5" cy="5" r="3.8" fill="none" stroke="#333" stroke-width="1.6"/><path d="M8 8l3 3" stroke="#333" stroke-width="1.8"/></svg></span></div>
</div>

<!-- Perks -->
<section class="perks">
  <div class="perk" style="left:114px">
    <h3>FREE<br>SHIPPING</h3><p>ALL ORDER OVER $250.00</p>
    <span class="perk-icon" style="background:var(--orange)"><svg width="28" height="28" viewBox="0 0 28 28"><path d="M26 14c0-1.2-1-2-2.2-2H17L11 3H8l3 9H6L4 9H2l1.5 5L2 19h2l2-3h5l-3 9h3l6-9h6.8c1.2 0 2.2-.8 2.2-2z" fill="#fff"/></svg></span>
  </div>
  <div class="perk" style="left:457px">
    <h3>BEST<br>PRODUCT</h3><p>ALL ORDER OVER $250.00</p>
    <span class="perk-icon" style="background:var(--grey-dark)"><svg width="26" height="26" viewBox="0 0 26 26"><rect x="4" y="8" width="18" height="15" fill="none" stroke="#fff" stroke-width="2.2"/><path d="M2 8h22M13 8v15" stroke="#fff" stroke-width="2.2"/><path d="M13 8c-2-5-7-5-6-1M13 8c2-5 7-5 6-1" fill="none" stroke="#fff" stroke-width="2"/></svg></span>
  </div>
  <div class="perk" style="left:800px">
    <h3>7 DAYS<br>RETURN</h3><p>ALL ORDER OVER $250.00</p>
    <span class="perk-icon" style="background:var(--grey-dark)"><svg width="28" height="28" viewBox="0 0 28 28"><path d="M7 9a9 9 0 11-1.5 8" fill="none" stroke="#fff" stroke-width="3"/><path d="M3 4v8h8z" fill="#fff"/></svg></span>
  </div>
</section>

<!-- Footer -->
<footer class="site-footer">
  <div class="footer-col" style="left:114px">
    <h4>SUPPORT</h4>
    <ul><li>Contact Us</li><li>Sizing Chart</li><li>Faq</li><li>Careers</li><li>Shipping</li><li>Returns</li></ul>
  </div>
  <div class="footer-col" style="left:354px">
    <h4>POPULAR LINKS</h4>
    <ul><li>Lingerie</li><li>Costumes</li><li>Panties</li><li>Dresses</li><li>Sleepwear</li><li>Hosiery</li><li>Accessories</li></ul>
  </div>
  <div class="footer-col" style="left:594px">
    <h4>FOLLOW US</h4>
    <div class="socials"><span></span><span></span><span></span><span></span></div>
    <h4 style="margin-top:26px">WE ACCEPT</h4>
    <div class="cards"><span style="background:#f2f2f2"></span><span style="background:#e9e9ef"></span><span style="background:#d9d9d9"></span></div>
  </div>
  <div class="footer-col" style="left:868px">
    <h4>NEWSLETTER</h4>
    <p class="news-text">Subscribe and be the first to hear news, offers and updates for the fullbloom community!</p>
    <div class="news-input">Your Email</div>
    <div class="news-btn">Subscribe</div>
  </div>
  <svg class="footer-wave" width="1200" height="130" viewBox="0 0 1200 130">
    <path d="M0 70 C300 78 560 92 820 60 C960 42 1080 20 1200 0 L1200 130 L0 130 Z" fill="var(--orange-deep)"/>
  </svg>
  <p class="copyright">Copyrights @ 2016. Fullbloom | All rights reserved</p>
  <div class="footer-brand">
    <div class="brand-name">FULLBLOOM</div>
    <div class="brand-tag">LINGERIE</div>
  </div>
</footer>

</body>
</html>
```